HOPE TABERNACLE- Premier Church Service.

Date: Sunday April 28th 2019.
Time: 10:30am-12:30pm
Venue: Blue Heron Hotel & conference Centre
4 N. Pellman Road Renton Wa 98064 USA.
Special treat at no extra cost!!!!
-Breakfast available 9am-10:15am.

-3 course Lunch available after Church.

NB: AMAZING ARRANGEMENTS FOR CHILDREN.
...........................................................................................................

EVENING JUBILEE, Wa 2019..........6:30pm-8:30pm.
" A time of high praise, deep Worship, the prophetic, Salvation, healing, miracles and more! "

...........................................................................................................................

Resident Pastors: Pastors Lou & Mary Kamau.

Guest ministers:

Apostle Daniel Otieno
Well of Mercy Sacramento, California.

THE LADY IN PINK IS THE WIFE TO THE MAN WITH THE ORANGE CLOTH IN HIS JACKET POSCKET. TRY MAKE IT COME OUT AS IF THESE TWO WERE TAKEN TOGETHER.

16-60

Designer to choose colors to be used in the design.

• -Very catchy and creative design.

```html
<!DOCTYPE html>
<html lang="en">
<head>
<meta charset="utf-8">
<title>Evening Jubilee, Wa 2019 – Hope Tabernacle</title>
<link rel="stylesheet" href="https://fonts.googleapis.com/css2?family=Roboto+Condensed:wght@700&family=Arimo:wght@400;700&family=Lato:wght@400&display=swap">
<style>
  :root {
    --stage: #333333;
    --paper: #ffffff;
    --yellow: #e4de00;
    --yellow-deep: #d6cf00;
    --purple: #a412b8;
    --purple-light: #c03ad0;
    --magenta: #b01ec0;
    --royal: #0d1fa0;
    --venue-blue: #1a2fb0;
    --ink: #111111;
  }
  html, body {
    margin: 0;
    width: 1200px;
    height: 1200px;
    overflow: hidden;
    background: var(--stage);
  }
  .flyer {
    position: absolute;
    left: 40px;
    top: 201px;
    width: 1120px;
    height: 797px;
    display: block;
  }
  .headline { font-family: "Roboto Condensed", "Arial Narrow", sans-serif; font-weight: 700; fill: var(--royal); }
  .time-pill-text { font-family: "Roboto Condensed", "Arial Narrow", sans-serif; font-weight: 700; fill: #fff; }
  .tagline { font-family: "Lato", Arial, sans-serif; font-size: 22px; fill: var(--ink); }
  .day { font-family: "Roboto Condensed", "Arial Narrow", sans-serif; font-weight: 700; fill: #fff; }
  .date { font-family: "Arimo", Arial, sans-serif; font-weight: 700; fill: var(--magenta); }
  .body { font-family: "Arimo", Arial, sans-serif; fill: var(--ink); }
  .children { font-family: "Roboto Condensed", "Arial Narrow", sans-serif; font-weight: 700; fill: var(--royal); }
  .strong { font-family: "Roboto Condensed", "Arial Narrow", sans-serif; font-weight: 700; }
  .venue-text { font-family: "Arimo", Arial, sans-serif; fill: #fff; }
</style>
</head>
<body>
<svg class="flyer" viewBox="0 0 1234 878" xmlns="http://www.w3.org/2000/svg">
  <defs>
    <linearGradient id="yellowSheen" x1="0" y1="0" x2="1" y2="1">
      <stop offset="0" stop-color="var(--yellow)"/>
      <stop offset="0.5" stop-color="#ebe51a"/>
      <stop offset="1" stop-color="var(--yellow-deep)"/>
    </linearGradient>
    <linearGradient id="purpleBox" x1="0" y1="0" x2="0" y2="1">
      <stop offset="0" stop-color="var(--purple-light)"/>
      <stop offset="1" stop-color="#8a0c9e"/>
    </linearGradient>
    <linearGradient id="hostsTone" x1="0" y1="0" x2="1" y2="1">
      <stop offset="0" stop-color="#6b4a3a"/>
      <stop offset="0.45" stop-color="#c9a6b8"/>
      <stop offset="1" stop-color="#e04ad8"/>
    </linearGradient>
    <linearGradient id="guestsTone" x1="0" y1="0" x2="1" y2="1">
      <stop offset="0" stop-color="#b9c8e0"/>
      <stop offset="0.6" stop-color="#8fa4c8"/>
      <stop offset="1" stop-color="#1c1c22"/>
    </linearGradient>
    <clipPath id="leftPanel">
      <path d="M0,0 L123,0 Q578,420 133,878 L0,878 Z"/>
    </clipPath>
    <clipPath id="rightPanel">
      <path d="M1133,0 C1060,70 985,150 950,240 C915,330 900,420 913,500 C930,650 1030,780 1158,878 L1234,878 L1234,0 Z"/>
    </clipPath>
  </defs>

  <!-- paper and centre band -->
  <rect class="paper" width="1234" height="878" fill="var(--paper)"/>
  <path class="centre-band" d="M123,0 L1133,0 C1060,70 985,150 950,240 C915,330 900,420 913,500 C930,650 1030,780 1158,878 L133,878 Q578,420 123,0 Z" fill="url(#yellowSheen)"/>

  <!-- host and guest portraits -->
  <g clip-path="url(#leftPanel)">
    <rect role="img" aria-label="Photo of resident pastors Lou and Mary Kamau standing together, he in a paisley jacket with an orange pocket square, she in pink" x="0" y="222" width="420" height="656" fill="url(#hostsTone)"/>
  </g>
  <g clip-path="url(#rightPanel)">
    <rect role="img" aria-label="Photo of guest minister Apostle Daniel Otieno in a light blue suit with his wife in black" x="880" y="280" width="354" height="598" fill="url(#guestsTone)"/>
  </g>

  <!-- curved borders -->
  <path d="M123,0 Q578,420 133,878" fill="none" stroke="var(--purple)" stroke-width="9"/>
  <path d="M1133,0 C1060,70 985,150 950,240 C915,330 900,420 913,500 C930,650 1030,780 1158,878" fill="none" stroke="var(--purple)" stroke-width="9"/>

  <!-- resident pastors -->
  <g class="residents">
    <text class="body" x="24" y="124" font-size="19">Resident Pastors:</text>
    <text class="body" x="24" y="158" font-size="33">Pastors Lou &amp;</text>
    <text class="body" x="24" y="194" font-size="33">Mary Kamau.</text>
  </g>

  <!-- meals -->
  <g class="meals">
    <text class="body" x="1015" y="162" font-size="19">Breakfast available</text>
    <text class="body strong" x="1015" y="188" font-size="24">9am–10:15am</text>
    <text class="body" x="983" y="230" font-size="19"><tspan class="strong">3 course Lunch</tspan> available</text>
    <text class="body" x="983" y="255" font-size="19">after Church.</text>
  </g>

  <!-- headline -->
  <text class="headline" x="635" y="100" font-size="82" text-anchor="middle" textLength="720" lengthAdjust="spacingAndGlyphs">EVENING JUBILEE, Wa 2019</text>

  <rect class="time-pill" x="363" y="127" width="497" height="93" rx="32" fill="url(#purpleBox)"/>
  <text class="time-pill-text" x="612" y="196" font-size="66" text-anchor="middle">6:30pm–8:30pm</text>

  <text class="tagline" x="626" y="260" text-anchor="middle">A time of high praise, deep Worship, the prophetic,</text>
  <text class="tagline" x="626" y="291" text-anchor="middle">Salvation, healing, miracles and more!</text>

  <!-- date -->
  <rect class="day-box" x="428" y="320" width="133" height="140" rx="24" fill="url(#purpleBox)"/>
  <text class="day" x="494" y="410" font-size="66" text-anchor="middle">Sun</text>
  <text class="date" x="590" y="367" font-size="50">April 28th</text>
  <text class="date" x="587" y="455" font-size="100">2019</text>

  <text class="body" x="626" y="508" font-size="32" text-anchor="middle">Time: 10:30am-12:30pm</text>

  <rect x="380" y="540" width="492" height="9" fill="var(--royal)"/>
  <rect x="380" y="556" width="492" height="4" fill="var(--purple)"/>

  <text class="body" x="612" y="607" font-size="30" text-anchor="middle">Special treat at no extra cost!!!!</text>
  <text class="children" x="622" y="666" font-size="31" text-anchor="middle">AMAZING ARRANGEMENTS FOR CHILDREN.</text>
  <rect x="393" y="689" width="464" height="2" fill="var(--royal)"/>

  <!-- guest ministers -->
  <text class="body" x="289" y="757" font-size="26">Guest Ministers</text>
  <rect x="505" y="718" width="2" height="82" fill="var(--ink)"/>
  <text class="body" x="524" y="748" font-size="25">Apostle Daniel Otieno</text>
  <text class="body" x="524" y="782" font-size="25">Well of Mercy Sacramento, California.</text>

  <!-- venue -->
  <rect class="venue" x="230" y="810" width="783" height="37" rx="18.5" fill="var(--venue-blue)"/>
  <text class="venue-text" x="621" y="835" font-size="19" text-anchor="middle" textLength="760" lengthAdjust="spacingAndGlyphs">Venue : Blue Heron Hotel &amp; conference Centre , 4 N. Pellman Road Renton Wa 98064 USA.</text>
</svg>
</body>
</html>
```